RK Bastone Construction Inc.

Design a new business card for our construction company
To be removed from current card:
Delete 25 years
Delete Tenant fit up Renovations section

```html
<!DOCTYPE html>
<html lang="en">
<head>
<meta charset="utf-8">
<title>RK Bastone Construction Inc. – Business Card</title>
<link rel="stylesheet" href="https://fonts.googleapis.com/css2?family=Open+Sans:wght@300;400;600;700&display=swap">
<style>
  :root {
    --purple: #62216f;
    --purple-dark: #3a1545;
    --purple-deep: #4b1958;
    --grey-icon: #77787b;
    --ink: #2b2b2b;
    --ink-soft: #4a4a4a;
    --paper: #ffffff;
    --backdrop: #e9e9ec;
  }
  * { margin: 0; padding: 0; box-sizing: border-box; }
  html, body {
    width: 1200px; height: 780px; overflow: hidden;
    background: var(--backdrop);
    font-family: "Open Sans", sans-serif;
  }
  .sheet {
    width: 1200px; height: 780px;
    display: flex; align-items: center; justify-content: center; gap: 40px;
  }
  .card {
    position: relative;
    width: 540px; height: 310px;
    background: var(--paper);
    border-radius: 14px;
    overflow: hidden;
    box-shadow: 0 6px 18px rgba(0,0,0,0.12);
  }
  .card__shapes { position: absolute; inset: 0; width: 100%; height: 100%; }
  .brand-name {
    position: absolute;
    color: var(--purple);
    font-weight: 700;
    text-transform: uppercase;
    line-height: 1.05;
    letter-spacing: 0.5px;
  }
  /* front */
  .card--front .brand-name { left: 200px; top: 52px; font-size: 30px; }
  .brand-name small { display: block; font-size: 0.55em; letter-spacing: 3px; margin-top: 4px; }
  .tagline {
    position: absolute; left: 202px; top: 140px;
    font-size: 11px; font-weight: 400; color: var(--ink-soft); letter-spacing: 0.6px;
  }
  .web-line {
    position: absolute; left: 250px; bottom: 26px;
    display: flex; align-items: center; gap: 8px;
    color: var(--paper); font-size: 14px; font-weight: 300; letter-spacing: 0.3px;
  }
  .web-line svg { width: 15px; height: 15px; }
  /* back */
  .card--back .brand-name { left: 26px; top: 30px; font-size: 23px; }
  .contact {
    position: absolute; left: 262px; top: 96px;
    display: flex; flex-direction: column; gap: 12px;
  }
  .contact__row { display: flex; align-items: center; gap: 12px; }
  .icon-badge {
    flex: none; width: 28px; height: 28px; border-radius: 50%;
    display: flex; align-items: center; justify-content: center;
  }
  .icon-badge--purple { background: var(--purple); }
  .icon-badge--grey { background: var(--grey-icon); }
  .icon-badge svg { width: 14px; height: 14px; }
  .person__name { font-size: 22px; color: var(--ink); line-height: 1; letter-spacing: 0.5px; text-transform: uppercase; }
  .person__name b { font-weight: 700; }
  .person__name span { font-weight: 300; }
  .person__role { font-size: 10px; color: var(--ink-soft); letter-spacing: 0.5px; margin-top: 3px; }
  .contact__text { font-size: 12px; color: var(--ink); line-height: 1.35; }
</style>
</head>
<body>
<main class="sheet">

  <!-- Front -->
  <section class="card card--front" aria-label="Business card front">
    <svg class="card__shapes" viewBox="0 0 540 310" preserveAspectRatio="none" aria-hidden="true">
      <polygon points="0,124 160,132 0,132" fill="var(--purple-dark)"/>
      <polygon points="0,132 160,132 225,232 540,254 540,310 0,310" fill="var(--purple)"/>
      <polygon points="225,232 540,280 540,310 170,310 160,300" fill="var(--purple-dark)"/>
    </svg>
    <div class="brand-name">RK Bastone<small>Construction Inc.</small></div>
    <p class="tagline">OFFICE | RETAIL | INSTITUTIONAL</p>
    <p class="web-line">
      <svg viewBox="0 0 16 16" fill="none" stroke="currentColor" stroke-width="1.2" aria-hidden="true">
        <circle cx="8" cy="8" r="6.5"/><ellipse cx="8" cy="8" rx="3" ry="6.5"/><line x1="1.5" y1="8" x2="14.5" y2="8"/>
      </svg>
      www.rkbastoneconstruction.ca
    </p>
  </section>

  <!-- Back -->
  <section class="card card--back" aria-label="Business card back">
    <svg class="card__shapes" viewBox="0 0 540 310" preserveAspectRatio="none" aria-hidden="true">
      <polygon points="0,150 120,162 0,162" fill="var(--purple-dark)"/>
      <polygon points="0,162 125,162 255,310 0,310" fill="var(--purple)"/>
    </svg>
    <div class="brand-name">RK Bastone<small>Construction Inc.</small></div>

    <div class="contact">
      <div class="contact__row">
        <span class="icon-badge icon-badge--purple">
          <svg viewBox="0 0 16 16" fill="#fff" aria-hidden="true"><circle cx="8" cy="5" r="3"/><path d="M2 15c0-3.5 2.7-5.5 6-5.5s6 2 6 5.5z"/></svg>
        </span>
        <div class="person">
          <p class="person__name"><b>Dario</b> <span>Bastone</span></p>
          <p class="person__role">FOUNDER | CEO</p>
        </div>
      </div>
      <div class="contact__row">
        <span class="icon-badge icon-badge--grey">
          <svg viewBox="0 0 16 16" fill="#fff" aria-hidden="true"><path d="M4 1.5l2.3 3-1.4 1.6c.8 1.9 2.2 3.3 4 4l1.6-1.4 3 2.3-1.2 2.5C7 13.6 2.4 9 1.5 3z"/></svg>
        </span>
        <p class="contact__text">613-555-0142<br>613-555-0187</p>
      </div>
      <div class="contact__row">
        <span class="icon-badge icon-badge--grey">
          <svg viewBox="0 0 16 16" fill="#fff" aria-hidden="true"><path d="M1 7.5L15 1.5 11.5 14.5 7.5 10 13 3.5 5.8 9z"/></svg>
        </span>
        <p class="contact__text">www.rkbastoneconstruction.ca</p>
      </div>
      <div class="contact__row">
        <span class="icon-badge icon-badge--purple">
          <svg viewBox="0 0 16 16" fill="#fff" aria-hidden="true"><path d="M8 1a5 5 0 0 0-5 5c0 3.8 5 9 5 9s5-5.2 5-9a5 5 0 0 0-5-5zm0 7a2 2 0 1 1 0-4 2 2 0 0 1 0 4z"/></svg>
        </span>
        <p class="contact__text">2180 Harlow Rd,<br>Suite 100, Ottawa, ON K1B 4T7</p>
      </div>
    </div>
  </section>

</main>
</body>
</html>
```